Integrative Medical Practice Website Redo

I am needing to have our current website redesigned to make it a responsive website to work on smartphones.
Current website
www.brightoakfm.com
Here are several examples of what I am looking for
https://www.corvanhealth.com/
I am wanting a popup for a newsletter signup
Looking for a very professional, clean, simple, minimalist, bold well designed website
Colors would ideally be greens and blues, cool tones, muted colors, or graytones like:
https://journeybright.org/
Several other clean design examples
http://7harborsrenton.com/
http://www.belvomedical.com/
http://sunpathyouth.com/
http://yourcellduke.com/
I would like the top navigation bar to be able to slide down while browsing site
We are also needing to add several features that are not on our current website:
Questionnaire buttons
Are you toxic questionnaire?
Take our hormone quiz to find out if hormones are affecting your health.
online scheduling option for:
nutrition counselling
testing like body composition, basal metabolic rate, CIMT, breast thermography, VO2 Max testing, Vita Trace
Therapies like whole body vibration, infrared sauna, Exercise with oxygen, hyperbaric oxygen, spinal decompression
Need to have separate page for different services and split up services into:
Consults/Office Visits, Testing, Therapies, Procedures
Need to have a button link to patient portal
Needs to have online store
Need to add navigation button "Start Here"
Need a spot for a video on practice summary
Newsletter signup to collect emails
Testimonials from linkpage
Blog that posts can be shared with social media
Password protected patient access that can integrate into crate.net ideally
Modules for programs online classes/videos
I have attached stock images that you can use, but feel free to find others to use.
I have also attached a copy of our current brochure that shows an overview of the practice
Target Market(s)
Health conscious people of all ages looking for a family medicine doctor
Industry/Entity Type
Alternative Medicine
Coding
Coded - Design and coding required
Number of Pages Required
5+ page
Look and feel

```html
<!DOCTYPE html>
<html lang="en">
<head>
<meta charset="utf-8">
<title>Modalities — Bright Oak Family Medicine</title>
<link rel="stylesheet" href="https://fonts.googleapis.com/css2?family=Lato:wght@400;700;900&display=swap">
<style>
:root{
  --sky:#3fb6de;
  --sky-dark:#34a8d3;
  --leaf:#7fc242;
  --leaf-dark:#5aa532;
  --ink:#4a4a4a;
  --body:#5b5b5b;
  --head:#555;
  --page:#f3f3f3;
  --white:#ffffff;
  --footer:#1f2a36;
  --footer-deep:#17202a;
  --footer-text:#c9d0d6;
}
*{box-sizing:border-box;margin:0;padding:0}
html,body{width:1200px;height:3000px;overflow:hidden}
body{font-family:'Lato',Arial,sans-serif;color:var(--body);background:var(--page);position:relative}
.abs{position:absolute}

/* top bar */
.topbar{left:0;top:0;width:1200px;height:28px;background:var(--sky);color:var(--white);font-size:11px;font-weight:700}
.topbar .item{position:absolute;top:7px;display:flex;align-items:center;gap:6px}
.topbar svg{width:12px;height:12px}
.cart-badge{display:inline-block;width:16px;height:16px;border-radius:50%;background:var(--leaf);text-align:center;line-height:16px;font-size:9px}

/* nav */
.navbar{left:0;top:28px;width:1200px;height:72px;background:var(--white)}
.brand{left:164px;top:12px;display:flex;align-items:center;gap:8px;color:var(--leaf-dark)}
.brand-dot{width:24px;height:24px;border-radius:50%;background:var(--leaf-dark)}
.brand-name{font-size:26px;font-weight:900;line-height:26px}
.brand-tag{font-size:9px;font-weight:900;letter-spacing:2px;line-height:12px;margin-top:2px}
.nav-links{left:558px;top:30px;display:flex;gap:0;font-size:12px;font-weight:700;color:var(--ink);letter-spacing:.5px}
.nav-links span{position:absolute;white-space:nowrap}
.search{left:1020px;top:28px;width:16px;height:16px}

/* content */
.page-title{left:164px;top:150px;font-size:24px;font-weight:900;letter-spacing:3px;color:var(--head)}
.photo{border-radius:0}
.mod-title{font-size:25px;color:var(--sky-dark);font-weight:400}
.copy{font-size:13px;line-height:17px;text-align:justify;color:var(--body)}
.copy p{margin-bottom:14px}
.rules-title{font-size:17px;color:var(--ink);font-weight:700}
.rules{font-size:12.5px;line-height:16px;color:var(--body)}
.rules p{margin-bottom:13px}
.sub-title{font-size:17px;font-weight:700;color:var(--ink);margin-bottom:2px}
.sub{margin-bottom:22px}
.sub .copy{text-align:left;font-size:12.5px;line-height:15.5px}

/* subscribe */
.subscribe{left:0;top:2530px;width:1200px;height:126px;background:var(--sky)}
.subscribe h3{position:absolute;top:26px;width:100%;text-align:center;color:var(--white);font-size:19px;font-weight:700}
.field{position:absolute;top:60px;height:32px;background:var(--white);font-size:10px;color:#999;padding:10px 0 0 30px}
.field svg{position:absolute;left:12px;top:11px;width:10px;height:10px}
.submit{position:absolute;top:60px;left:740px;width:158px;height:32px;background:var(--leaf);color:var(--white);font-weight:900;font-size:15px;letter-spacing:2px;text-align:center;line-height:32px}

/* footer */
.footer{left:0;top:2656px;width:1200px;height:344px;background:linear-gradient(180deg,#24303c,#1b2530)}
.footer-bottom{left:0;top:2968px;width:1200px;height:32px;background:var(--footer-deep)}
.f-head{font-size:13px;font-weight:700;letter-spacing:1.5px;color:var(--white)}
.fb-box{left:180px;top:2732px;width:232px;height:190px;background:var(--white);border:1px solid #ddd}
.fb-cover{left:0;top:0;width:230px;height:66px;background:linear-gradient(135deg,#c9b8a6,#8fa7bf)}
.fb-name{left:86px;top:12px;color:var(--white);font-size:16px;font-weight:700}
.fb-likes{left:86px;top:32px;color:var(--white);font-size:9px}
.fb-thumb{left:10px;top:10px;width:66px;height:66px;background:linear-gradient(135deg,#e6d4c3,#a7b7c6);border:2px solid var(--white)}
.fb-btn{top:84px;height:20px;border:1px solid #ccc;background:#f6f7f9;font-size:10px;color:#333;padding:3px 8px}
.fb-friends{left:10px;top:122px;font-size:10px;color:#333}
.fb-row{left:10px;top:140px;display:flex;gap:6px}
.fb-row div{width:30px;height:30px}
.info-list{left:450px;top:2728px;font-size:11.5px;color:var(--footer-text);line-height:22px;list-style:none}
.info-list li::before{content:"▸";color:var(--white);margin-right:12px;font-size:9px}
.f-brand{left:814px;top:2692px;display:flex;align-items:center;gap:8px;color:var(--leaf)}
.f-contact{left:818px;font-size:11px;color:var(--footer-text);display:flex;align-items:center;gap:12px}
.f-contact svg{width:12px;height:12px}
.socials{left:820px;top:2896px;display:flex;gap:12px}
.socials div{width:30px;height:30px;border-radius:50%;background:var(--leaf)}
.copyright{right:172px;top:2978px;font-size:9.5px;color:var(--footer-text)}
</style>
</head>
<body>

<header>
  <div class="abs topbar">
    <div class="item" style="left:164px">
      <svg viewBox="0 0 12 12"><path d="M3 1l2 2-1 1.5c.8 1.6 1.9 2.7 3.5 3.5L9 7l2 2-1.5 2C5.5 10.5 1.5 6.5 1 2.5z" fill="#fff"/></svg>(555) 210-4477</div>
    <div class="item" style="left:276px">
      <svg viewBox="0 0 12 12"><rect x="1" y="2.5" width="10" height="7" fill="none" stroke="#fff" stroke-width="1.2"/><path d="M1 3l5 4 5-4" fill="none" stroke="#fff" stroke-width="1.2"/></svg>support@brightoak.com</div>
    <div class="item" style="left:424px">
      <svg viewBox="0 0 12 12"><circle cx="6" cy="6" r="5" fill="none" stroke="#fff" stroke-width="1.2"/><path d="M6 3v3l2 1.5" stroke="#fff" fill="none" stroke-width="1.2"/></svg>Mon - Sat 9:00 - 19:00</div>
    <div class="item" style="left:872px">LOGIN &nbsp;|&nbsp; REGISTER</div>
    <div class="item" style="left:1000px">
      <svg viewBox="0 0 12 12"><path d="M1 2h2l1.5 6h6L12 4H4" fill="none" stroke="#fff" stroke-width="1.2"/><circle cx="5" cy="10" r="1" fill="#fff"/><circle cx="9.5" cy="10" r="1" fill="#fff"/></svg><span class="cart-badge">0</span></div>
  </div>

  <nav class="abs navbar">
    <div class="abs brand">
      <div class="brand-dot"></div>
      <div>
        <div class="brand-name">Bright Oak</div>
        <div class="brand-tag">FAMILY MEDICINE</div>
      </div>
    </div>
    <div class="abs nav-links">
      <span style="left:0">HOME</span>
      <span style="left:64px">ABOUT</span>
      <span style="left:132px">SERVICES</span>
      <span style="left:218px">TESTIMONIALS</span>
      <span style="left:332px">BLOG</span>
      <span style="left:386px">CONTACT</span>
    </div>
    <svg class="abs search" viewBox="0 0 16 16"><circle cx="6.5" cy="6.5" r="5" fill="none" stroke="#333" stroke-width="2"/><path d="M10.5 10.5L15 15" stroke="#333" stroke-width="2.2"/></svg>
  </nav>
</header>

<main>
  <h1 class="abs page-title">MODALITIES</h1>

  <!-- Family Medicine -->
  <section>
    <div class="abs photo" role="img" aria-label="Smiling family with a doctor in a white coat" style="left:164px;top:236px;width:442px;height:308px;background:linear-gradient(135deg,#d9dfe3,#c8b7a3 55%,#e8e4df)"></div>
    <h2 class="abs mod-title" style="left:632px;top:238px">Family Medicine</h2>
    <div class="abs copy" style="left:632px;top:282px;width:410px">
      <p>In addition to what you would expect from any family medicine clinic, we utilize many different modalities in our attempt to improve your quality of health, whether it is pharmaceutical or nutraceutical.</p>
      <p>Routine primary care is provided for newborns to adults. We do everything that a primary care practice does plus we deliver it in an integrative way. This includes routine physicals, gynecological care (including pap smears), same day visits for acute conditions, and chronic disease management.</p>
    </div>
  </section>

  <!-- Manipulation -->
  <section>
    <div class="abs photo" role="img" aria-label="Patient lying down receiving a neck and head manipulation" style="left:164px;top:588px;width:442px;height:294px;background:linear-gradient(135deg,#1a1410,#6b4a36 50%,#d4b49a)"></div>
    <h2 class="abs mod-title" style="left:632px;top:584px">Manipulation</h2>
    <div class="abs copy" style="left:632px;top:626px;width:410px">
      <p>Dr. Marlow is a practicing Osteopathic Physician and, as such, has been trained in manual manipulation. He had learned about manipulation, long before medical school from his father who is a chiropractor.</p>
      <p>He has studied with some of this country's best doctors who specialize in manipulation, has attended many courses and conferences regarding manipulation, and utilizes many different techniques, from cranial treatments to high velocity adjustments.</p>
    </div>
  </section>

  <!-- Nutrition -->
  <section>
    <div class="abs photo" role="img" aria-label="Woman with a measuring tape around her waist behind fresh fruit and vegetables" style="left:164px;top:944px;width:442px;height:296px;background:linear-gradient(180deg,#f2ede8,#e6d2c2 45%,#8fbf5a 75%,#d8483a)"></div>
    <h2 class="abs mod-title" style="left:632px;top:938px">Nutrition</h2>
    <div class="abs copy" style="left:632px;top:980px;width:410px">
      <p>&nbsp;Having a bachelor's degree in Nutritional Science, Dr. Marlow has the conviction that nutrition is one of the keys to optimal health, since nutrition has an effect on one's body every day. Nutrition is not traditionally taught in medical schools, so many physicians fall short in treatment of many chronic conditions, as most medications are not designed for long-term therapy. The phrase "You are what you eat" is truer than what one might think.</p>
      <p>Daniel Herrow's quote, "Eat food. Not too much. Mostly plants", is a great adage by which to live. Probably, the first two words are most important. "Eat food" means to eat healthy food ... vegetables, fruits, whole grains, and, yes, fish and meat, and to avoid what Herrow calls "edible food-like substances".</p>
      <p>You are either improving or damaging your health with what you eat.</p>
    </div>

    <h3 class="abs rules-title" style="left:160px;top:1256px">Daniel Herrow's "7 Rules for Eating"</h3>
    <div class="abs rules" style="left:164px;top:1286px;width:880px">
      <p>1. Don't eat anything your great-grandmother wouldn't recognize as food. When you pick up that box of portable yogurt tubes, or eat something with 15 ingredients you can't pronounce, ask yourself, "What are those things doing there?"</p>
      <p>2. Don't eat anything with more than five ingredients, or with ingredients you can not pronounce.</p>
      <p>3. Stay out of the middle of supermarkets and, instead, shop on the perimeter of the stores. Real foods tends to be on the outer perimeter of the store near the loading docks, where items can be replaced with fresh foods when they reach expiration.</p>
      <p>4. Don't eat anything that won't eventually rot. There are exceptions, such as honey, but as a rule, items, such as "Fluffins", which do not spoil, are not foods.</p>
      <p>5. It is not only what you eat, but how you eat. Always leave the table a little hungry. Many cultures have a rule that one stops eating before one is full. In Japan, they say, "Eat until you are four-fifths full." Islamic culture has a similar rule, and in German culture they say, "Tie off the sack before it's full."</p>
      <p>6. Families used to traditionally dine together, around a table, not a television, and at regular meal times. It's a good tradition. Enjoy meals with the people you love. "Remember when eating between meals felt wrong?" Herrow asked.</p>
      <p>7. Don't buy food where you buy your gasoline. In the U.S., 20% of food is eaten in the car.</p>
    </div>
  </section>

  <!-- Acupuncture -->
  <section>
    <div class="abs photo" role="img" aria-label="Acupuncture needles and green capsules on a wooden table" style="left:164px;top:1652px;width:442px;height:300px;background:linear-gradient(135deg,#8a6a4e,#b89470 45%,#a6b860 60%,#6e5038)"></div>
    <h2 class="abs mod-title" style="left:626px;top:1644px">Acupuncture</h2>
    <div class="abs copy" style="left:626px;top:1702px;width:414px">
      <p style="margin-bottom:0">Medical acupuncture provides many types of approaches that are used depending on the individual and their needs, such as, pain management, energy balancing, or treating a systemic condition versus local condition. Dr Marlow has studied with numerous acupuncturists, and he utilizes several different types of acupuncture, including French Energetics, Traditional Chinese Medicine, Auricular Acupuncture, YNSA, and Five Element.</p>
      <p style="margin-bottom:0">Auricular Acupuncture</p>
      <p>Auricular acupuncture is based on a reflex somatotopic system organized on the surface of the external ear. The external ear is unique in that it is structured from tissue from each of the three embryonic layers in the early development of an infant and has connections to the nervous system. This method is frequently used as an adjunct to other acupuncture methods and is especially useful for pain, metabolic disorders, central nervous system disorders, behavioral issues and addiction.</p>
    </div>

    <div class="abs" style="left:164px;top:1976px;width:880px">
      <div class="sub">
        <h3 class="sub-title">Chinese Scalp Acupuncture</h3>
        <p class="copy">Scalp acupuncture is a modern acupuncture method developed in China that combines traditional needling methods with modern knowledge of the brain anatomy. This method is especially useful for central nervous system disorders such as stroke, paralysis, back pain, phantom limb pain and multiple sclerosis.</p>
      </div>
      <div class="sub">
        <h3 class="sub-title">Energetic Acupuncture</h3>
        <p class="copy">Acupuncture needlesThis approach uses the Yin and Yang channels that are part of the energy circuits in the body called Principal Meridians. Principal Meridians are the largest energy circuits that pass between and through the muscles of the body and send energy branches to the internal organs. Many acupuncture energy subsystems stem from these Principal Meridians and can be activated through specific needling techniques. Acupuncture treatment protocols use a specific needle input to affect the energy of the entire body.<br>Treatment is often based on the patient's constitutional tendencies, or biopsychotypes, that influence their life and health. To learn more about your biopsychotype, visit Dr. Owen Falk's "Learning More About You" questionnaire and bring to your acupuncture appointment.</p>
      </div>
      <div class="sub">
        <h3 class="sub-title">Five Element Constitutional Acupuncture</h3>
        <p class="copy">This is an acupuncture method that emphasizes the diagnosis and treatment of a primary constitutional imbalance in the patient based on the the Five Elements as described in ancient acupuncture texts. The treatment places priority on the health of the person's body, mind and spirit. It strives to identify blocks that may be adversely affecting a person's body, mind and spirit and stresses preventative treatments.</p>
      </div>
      <div class="sub">
        <h3 class="sub-title">Pain Management</h3>
        <p class="copy">Acupuncture needles inserted in backVarious acupuncture methods are available for approaching musculoskeletal pain that range from approaches at the surface fascial nodules to deeper muscle spasm myofascial trigger points to spinal nerve segments. A treatment plan will often start with the most superficial level and then increase in depth and intensity as needed. Frequently, a few treatments are given in the first two weeks and then spread out in frequency to bi-weekly for one to two treatments and then every one to three months, or as needed.</p>
      </div>
      <div class="sub">
        <h3 class="sub-title">Percutaneous Nerve Stimulation</h3>
        <p class="copy">Percutaneous nerve stimulation involves using sequential or simultaneous electro-acupuncture for treatment of chronic musculoskeletal pain that affects the spinal nerve segments. This method uses unique electro-acupuncture frequencies to provoke the release of neurotransmitters involved in pain modulation (such as, serotonin, norepinephrine, substance P, GABA and dopamine).</p>
      </div>
    </div>
  </section>
</main>

<section class="abs subscribe">
  <h3>Have Questions ? Feel free to Subscribe for Latest News &amp; Updates.</h3>
  <div class="field" style="left:304px;width:210px">
    <svg viewBox="0 0 10 10"><circle cx="5" cy="3" r="2.2" fill="#999"/><path d="M1 10c0-3 8-3 8 0z" fill="#999"/></svg>Full Name</div>
  <div class="field" style="left:522px;width:210px">
    <svg viewBox="0 0 10 10"><rect x="0.5" y="2" width="9" height="6" fill="none" stroke="#999"/><path d="M.5 2.5L5 6l4.5-3.5" fill="none" stroke="#999"/></svg>Email Address</div>
  <div class="submit">SUBMIT</div>
</section>

<footer>
  <div class="abs footer"></div>
  <div class="abs footer-bottom"></div>

  <h4 class="abs f-head" style="left:176px;top:2688px">LIKE US ON LINKPAGE</h4>
  <div class="abs fb-box">
    <div class="abs fb-cover" role="img" aria-label="Page cover photo"></div>
    <div class="abs fb-thumb" role="img" aria-label="Page profile photo"></div>
    <div class="abs fb-name">Page Name</div>
    <div class="abs fb-likes">36 likes</div>
    <div class="abs fb-btn" style="left:10px">✓ Liked</div>
    <div class="abs fb-btn" style="left:160px">↪ Share</div>
    <div class="abs fb-friends">You and 36 other friends like this</div>
    <div class="abs fb-row" role="img" aria-label="Friend profile photos">
      <div style="background:#c7a88c"></div><div style="background:#8aa2bd"></div><div style="background:#6d7f8f"></div><div style="background:#b9c4cf"></div><div style="background:#a08770"></div><div style="background:#7e93a8"></div>
    </div>
  </div>

  <h4 class="abs f-head" style="left:450px;top:2688px">INFORMATION</h4>
  <ul class="abs info-list">
    <li>Services</li><li>About Us</li><li>Forum</li><li>Help center</li><li>FAQ</li><li>Privacy Policy</li><li>Resources</li><li>Contact</li>
  </ul>

  <div class="abs f-brand">
    <div class="brand-dot" style="background:var(--leaf)"></div>
    <div>
      <div class="brand-name">Bright Oak</div>
      <div class="brand-tag">FAMILY MEDICINE</div>
    </div>
  </div>
  <div class="abs f-contact" style="top:2778px">
    <svg viewBox="0 0 12 12"><path d="M6 11S2 6.5 2 4.5a4 4 0 018 0C10 6.5 6 11 6 11z" fill="#fff"/><circle cx="6" cy="4.5" r="1.4" fill="#24303c"/></svg>4810 Linden Way, Fairview, TX 79000</div>
  <div class="abs f-contact" style="top:2804px">
    <svg viewBox="0 0 12 12"><rect x="1" y="2.5" width="10" height="7" fill="#fff"/><path d="M1 3l5 4 5-4" fill="none" stroke="#24303c"/></svg>info@brightoak.com</div>
  <div class="abs f-contact" style="top:2830px">
    <svg viewBox="0 0 12 12"><path d="M3 1l2 2-1 1.5c.8 1.6 1.9 2.7 3.5 3.5L9 7l2 2-1.5 2C5.5 10.5 1.5 6.5 1 2.5z" fill="#fff"/></svg>(555) 210-4477</div>
  <h4 class="abs f-head" style="left:820px;top:2870px;font-size:10px">FOLLOW US</h4>
  <div class="abs socials"><div></div><div></div><div></div><div></div><div></div></div>

  <p class="abs copyright">Copyright © 2016. Bright Oak. All Rights Reserved.</p>
</footer>

</body>
</html>
```